Restaurant service company needs a website!

I am looking for a skilled web designer/developer to create a professional, responsive, and easy-to-navigate website for my company, which specializes in servicing restaurant cooking equipment. The site should communicate trust, reliability, and technical expertise to our target audience, restaurant owners, managers, and commercial kitchen operators. I have included the company logos, if any other format for them is needed please let me know.

Target Market(s)

restaurant owners, managers, and commercial kitchen operators

Industry/Entity Type

Commercial Kitchen Equipment Service

Coding

Coded - Design and coding required

Number of Pages Required

1 page

Font styles to use
Serif
Sans Serif

Requirements
Must have
• Contact and service request forms, Click-to-call functionality for mobile, Clean, modern layout with strong visuals, Easy navigation, mobile-friendly
Nice to have
• Testimonials or Reviews, If possible a click-to-text functionality for mobile.
Should not have
• Any mention of Refrigeration or HVAC, "Free Quotes"

```html
<!DOCTYPE html>
<html lang="en">
<head>
<meta charset="utf-8">
<title>Kettlepoint</title>
<link href="https://fonts.googleapis.com/css2?family=Montserrat:wght@500;600;700&family=Lato:ital,wght@0,400;0,700;1,400&family=Roboto:wght@400;500&display=swap" rel="stylesheet">
<style>
:root{
  --brand:#0d6079;
  --band:#e2f1f6;
  --ink:#1d1d1f;
  --body:#3b3b3b;
  --white:#ffffff;
}
*{box-sizing:border-box;margin:0;padding:0}
html,body{width:1200px;height:3411px;overflow:hidden}
body{position:relative;background:var(--white);font-family:'Lato',sans-serif;color:var(--ink)}
a{text-decoration:none;color:inherit}
.abs{position:absolute}
svg{display:block}

/* header */
.site-header{left:0;top:0;width:1200px;height:86px;background:var(--white)}
.brand{left:104px;top:26px;display:flex;align-items:center;gap:10px}
.brand-dot{width:16px;height:16px;background:var(--brand)}
.brand-name{font-family:'Montserrat',sans-serif;font-weight:700;font-size:28px;color:var(--brand);line-height:34px}
.nav{top:33px;font-family:'Roboto',sans-serif;font-size:15px;color:var(--ink)}
.nav.active{color:var(--brand);text-decoration:underline}
.call-btn{left:907px;top:20px;width:180px;height:47px;background:var(--brand);border-radius:3px;color:var(--white);font-family:'Roboto',sans-serif;font-size:15px;display:flex;align-items:center;justify-content:center;gap:12px}

/* hero */
.hero{left:0;top:86px;width:1200px;height:514px;background:linear-gradient(100deg,#9c9b92 0%,#bdbdb4 35%,#c9cbc6 55%,#8fa0b8 75%,#d6d8d8 100%)}
.hero-shade{left:0;top:86px;width:700px;height:514px;background:linear-gradient(90deg,rgba(60,60,55,.35),rgba(0,0,0,0))}
.hero-title{left:109px;top:162px;font-family:'Montserrat',sans-serif;font-weight:700;font-size:51px;line-height:60px;color:var(--white);text-shadow:0 2px 6px rgba(0,0,0,.35)}
.btn{background:var(--brand);color:var(--white);font-family:'Lato',sans-serif;font-weight:700;font-size:17px;display:flex;align-items:center;justify-content:center;border-radius:3px}

/* section titles */
.section-title{left:0;width:1200px;text-align:center;font-family:'Montserrat',sans-serif;font-weight:500;font-size:40px;color:var(--ink)}
.section-title b{font-weight:700;color:var(--brand)}

/* service cards */
.card{width:307px;background:var(--white);border:2px solid #e4e4e4;border-radius:6px;box-shadow:0 2px 8px rgba(0,0,0,.06)}
.service-card{top:752px;height:296px}
.service-icon{position:absolute;left:23px;top:25px;width:107px;height:93px;background:var(--brand);border-radius:5px;display:flex;align-items:center;justify-content:center}
.service-name{position:absolute;left:22px;top:134px;font-family:'Lato',sans-serif;font-weight:700;font-size:21px;color:var(--ink)}
.service-text{position:absolute;left:23px;top:172px;width:262px;font-size:14.5px;line-height:26px;color:var(--body)}
.read-more{position:absolute;left:23px;top:263px;font-style:italic;font-size:14px;color:var(--ink)}

/* about */
.about-band{left:0;top:1132px;width:1200px;height:535px;background:var(--band)}
.about-frame{left:110px;top:1216px;width:448px;height:367px;border:2px solid var(--brand);border-radius:4px}
.about-photo{left:126px;top:1234px;width:446px;height:366px;border-radius:4px;background:linear-gradient(135deg,#8d7d6c 0%,#b7a58e 40%,#6d7f96 65%,#c9b7a1 100%);box-shadow:0 4px 10px rgba(0,0,0,.2)}
.about-title{left:645px;top:1208px;font-family:'Montserrat',sans-serif;font-weight:500;font-size:40px}
.about-title b{color:var(--brand);font-weight:700}
.about-text{left:645px;width:444px;font-size:14.5px;line-height:25.7px;color:var(--body);text-align:justify}

/* why */
.why-label{top:1997px;width:200px;text-align:center;font-family:'Roboto',sans-serif;font-weight:500;font-size:15px;color:var(--ink)}

/* testimonials */
.reviews-band{left:0;top:2102px;width:1200px;height:527px;background:var(--band)}
.review-card{top:2254px;height:293px}
.stars{position:absolute;left:22px;top:28px;display:flex;gap:2px}
.review-text{position:absolute;left:22px;top:78px;width:266px;font-size:14.5px;line-height:26.5px;color:var(--body)}
.avatar{position:absolute;left:22px;top:191px;width:70px;height:70px;border-radius:50%;background:linear-gradient(160deg,#d8d2cc,#7b6a5e)}
.reviewer{position:absolute;left:110px;top:204px;font-family:'Roboto',sans-serif;font-size:17px;line-height:25px;color:var(--ink)}
.arrow{width:28px;height:28px;border-radius:50%;display:flex;align-items:center;justify-content:center}

/* form */
.field{height:48px;background:var(--white);border-radius:4px;box-shadow:0 2px 8px rgba(0,0,0,.13);display:flex;align-items:center;padding-left:22px;gap:12px;font-family:'Lato',sans-serif;font-size:15px;color:#6b6b6b}

/* footer */
.site-footer{left:0;top:3056px;width:1200px;height:355px;background:var(--brand)}
.foot-brand{left:110px;top:3200px;color:var(--white);font-family:'Montserrat',sans-serif;font-weight:700;font-size:26px}
.social{top:3318px;width:21px;height:21px;border-radius:50%;background:var(--white)}
.foot-head{top:3136px;font-family:'Montserrat',sans-serif;font-weight:500;font-size:19px;color:var(--white)}
.foot-list{list-style:none;font-family:'Roboto',sans-serif;font-size:16px;color:var(--white)}
.foot-list li{height:34.4px;display:flex;align-items:center;gap:14px}
.foot-list li.sq::before{content:"";width:7px;height:7px;background:var(--white)}
.foot-rule{left:110px;top:3364px;width:979px;height:1px;background:rgba(255,255,255,.45)}
.copyright{left:0;top:3376px;width:1200px;text-align:center;font-family:'Roboto',sans-serif;font-size:13px;color:var(--white)}
</style>
</head>
<body>

<header class="abs site-header">
  <div class="abs brand"><span class="brand-dot"></span><span class="brand-name">Kettlepoint</span></div>
  <span class="abs nav active" style="left:479px">Home</span>
  <span class="abs nav" style="left:545px">About</span>
  <span class="abs nav" style="left:611px">Services</span>
  <span class="abs nav" style="left:691px">Testimonials</span>
  <span class="abs nav" style="left:799px">Contact Us</span>
  <a class="abs call-btn" href="tel:+15550100199">
    <svg width="22" height="22" viewBox="0 0 24 24"><path fill="#fff" d="M6.6 10.8a15 15 0 0 0 6.6 6.6l2.2-2.2c.3-.3.7-.4 1-.2 1.1.4 2.3.6 3.6.6.6 0 1 .4 1 1V20c0 .6-.4 1-1 1A17 17 0 0 1 3 4c0-.6.4-1 1-1h3.5c.6 0 1 .4 1 1 0 1.3.2 2.5.6 3.6.1.3 0 .7-.2 1z"/><path fill="none" stroke="#fff" stroke-width="1.6" d="M14 3.5a7 7 0 0 1 6.5 6.5M14 7a3.5 3.5 0 0 1 3 3"/></svg>
    +1 555 010 0199
  </a>
</header>

<section>
  <div class="abs hero" role="img" aria-label="Technician in blue overalls servicing a kitchen range hood, with an open red toolbox in the foreground"></div>
  <div class="abs hero-shade"></div>
  <h1 class="abs hero-title">Reliable Cooking<br>Equipment Service<br>You Can Trust</h1>
  <a class="abs btn" style="left:109px;top:371px;width:164px;height:46px">Request Service</a>
</section>

<section>
  <h2 class="abs section-title" style="top:670px">Our <b>Services</b></h2>

  <article class="abs card service-card" style="left:109px">
    <div class="service-icon"><svg width="60" height="60" viewBox="0 0 60 60"><g fill="none" stroke="#fff" stroke-width="5"><circle cx="28" cy="28" r="12"/><path d="M28 8v6M28 42v6M8 28h6M42 28h6M14 14l4 4M38 38l4 4M42 14l-4 4M14 42l4-4"/></g><path d="M34 34l14 14" stroke="#fff" stroke-width="6" stroke-linecap="round"/></svg></div>
    <h3 class="service-name">Equipment Repairs</h3>
    <p class="service-text">Fast, reliable repairs for commercial cooking equipment. From ovens and grills to fryers and ranges, our expert</p>
    <span class="read-more">Read More...</span>
  </article>

  <article class="abs card service-card" style="left:446px">
    <div class="service-icon"><svg width="58" height="60" viewBox="0 0 58 60"><rect x="8" y="8" width="34" height="46" rx="3" fill="none" stroke="#fff" stroke-width="4"/><path d="M14 20l3 3 5-6M14 32l3 3 5-6M14 44l3 3 5-6M26 21h10M26 33h10M26 45h10" fill="none" stroke="#fff" stroke-width="3"/><circle cx="46" cy="14" r="7" fill="none" stroke="#fff" stroke-width="3"/></svg></div>
    <h3 class="service-name">Preventive Maintenance</h3>
    <p class="service-text">Fast, reliable repairs for commercial cooking equipment. From ovens and grills to fryers and ranges, our expert</p>
    <span class="read-more">Read More...</span>
  </article>

  <article class="abs card service-card" style="left:783px">
    <div class="service-icon"><svg width="60" height="60" viewBox="0 0 60 60"><circle cx="30" cy="30" r="15" fill="none" stroke="#fff" stroke-width="4"/><path d="M30 22v10" stroke="#fff" stroke-width="4" stroke-linecap="round"/><circle cx="30" cy="38" r="2.4" fill="#fff"/><path d="M10 32a20 20 0 0 1 40 0" fill="none" stroke="#fff" stroke-width="4"/><rect x="6" y="28" width="8" height="14" rx="3" fill="#fff"/><rect x="46" y="28" width="8" height="14" rx="3" fill="#fff"/><path d="M50 42c0 8-8 10-14 10" fill="none" stroke="#fff" stroke-width="3"/></svg></div>
    <h3 class="service-name">Emergency Support</h3>
    <p class="service-text">Fast, reliable repairs for commercial cooking equipment. From ovens and grills to fryers and ranges, our expert</p>
    <span class="read-more">Read More...</span>
  </article>
</section>

<section>
  <div class="abs about-band"></div>
  <div class="abs about-frame"></div>
  <div class="abs about-photo" role="img" aria-label="Technician in a cap and gloves repairing a commercial espresso machine"></div>
  <h2 class="abs about-title">About <b>Us</b></h2>
  <p class="abs about-text" style="top:1268px;text-align:left">At Kettlepoint, we understand how critical reliable equipment is to your restaurant’s success. A single breakdown can disrupt service, frustrate customers, and impact your bottom line. That’s why we specialize in keeping your cooking equipment running at its best.</p>
  <p class="abs about-text" style="top:1384px">With years of experience in the industry, our skilled technicians provide expert repairs, preventive maintenance, and responsive emergency support for commercial kitchens. We partner with restaurants, cafés, and foodservice operators to ensure their kitchens run smoothly — day after day.</p>
  <a class="abs btn" style="left:645px;top:1536px;width:127px;height:46px">Read More</a>
</section>

<section>
  <h2 class="abs section-title" style="top:1740px">Why <b>Choose Kettlepoint</b></h2>
  <svg class="abs" style="left:0;top:1826px" width="1200" height="160" viewBox="0 0 1200 160">
    <defs>
      <g id="ring"><circle r="78" fill="#fff" stroke="#d9d9d9" stroke-width="2"/><path d="M0 78A78 78 0 0 1 0 -78" fill="none" stroke="#0d6079" stroke-width="3"/></g>
    </defs>
    <g fill="#0d6079">
      <g transform="translate(188 79)"><use href="#ring"/><circle cx="0" cy="-14" r="11"/><path d="M-6 -14l4 4 8-8" stroke="#fff" stroke-width="3" fill="none"/><path d="M-32 10l14-8 12 6 8-4 14 4 16 4-6 14-12 8-18 4-14-8z"/></g>
      <g transform="translate(392 79)"><use href="#ring"/><circle cx="0" cy="-4" r="12"/><circle cx="-18" cy="4" r="7"/><circle cx="18" cy="4" r="7"/><path d="M-16 30a16 16 0 0 1 32 0z"/><path d="M-12 -26l3 6M0 -30v7M12 -26l-3 6" stroke="#0d6079" stroke-width="3"/></g>
      <g transform="translate(597 79)"><use href="#ring"/><path d="M-4 -30c10 0 18 8 14 18l14 14-8 8-14-14c-10 4-18-4-18-14l8 6 6-6z"/><circle cx="0" cy="14" r="10" fill="none" stroke="#0d6079" stroke-width="4"/><path d="M-30 -6h14M-34 4h14M-30 14h12" stroke="#0d6079" stroke-width="3"/></g>
      <g transform="translate(803 79)"><use href="#ring"/><circle r="22"/><g stroke="#0d6079" stroke-width="10"><path d="M0 -32v64M-32 0h64M-23 -23l46 46M23 -23l-46 46"/></g><circle r="15" fill="#fff"/><path d="M-8 0l6 6 10-11" stroke="#0d6079" stroke-width="4" fill="none"/></g>
      <g transform="translate(1009 79)"><use href="#ring"/><circle cx="0" cy="4" r="8"/><path d="M-14 26a14 14 0 0 1 28 0z"/><circle cx="-20" cy="10" r="6"/><circle cx="20" cy="10" r="6"/><path d="M-32 28a12 12 0 0 1 22 0zM10 28a12 12 0 0 1 22 0z"/><path d="M0 -24v14M-6 -14l6 6 6-6" stroke="#0d6079" stroke-width="3" fill="none"/></g>
    </g>
  </svg>
  <span class="abs why-label" style="left:88px">Trusted by Restaurants</span>
  <span class="abs why-label" style="left:292px">Expert Technicians</span>
  <span class="abs why-label" style="left:497px">Fast &amp; Reliable Service</span>
  <span class="abs why-label" style="left:703px">Maintenance Focus</span>
  <span class="abs why-label" style="left:909px">Trusted by Restaurants</span>
</section>

<section>
  <div class="abs reviews-band"></div>
  <h2 class="abs section-title" style="top:2166px">What Our <b>Clients Say</b></h2>

  <svg width="0" height="0" style="position:absolute"><defs><path id="star" d="M9 0l2.7 5.6 6.1.8-4.5 4.3 1.1 6.1L9 13.9 3.6 16.8l1.1-6.1L.2 6.4l6.1-.8z" fill="#f59a12"/></defs></svg>

  <article class="abs card review-card" style="left:109px">
    <div class="stars"><svg width="94" height="18"><use href="#star"/><use href="#star" x="19"/><use href="#star" x="38"/><use href="#star" x="57"/><use href="#star" x="76"/></svg></div>
    <p class="review-text">Kettlepoint saved us during our busiest dinner rush. Their technician arrived quickly, fixed the problem, and had us back in service in no time. Truly reliable.</p>
    <div class="avatar" role="img" aria-label="Portrait photo of the reviewer"></div>
    <p class="reviewer">Marisa<br>Restaurant Owner</p>
  </article>

  <article class="abs card review-card" style="left:446px">
    <div class="stars"><svg width="94" height="18"><use href="#star"/><use href="#star" x="19"/><use href="#star" x="38"/><use href="#star" x="57"/><use href="#star" x="76"/></svg></div>
    <p class="review-text">We've been using Kettlepoint for regular maintenance, and it has made all the difference. Our kitchen runs smoother, and we've avoided major breakdowns.</p>
    <div class="avatar" role="img" aria-label="Portrait photo of the reviewer"></div>
    <p class="reviewer">Daniel P.,<br>Kitchen Manager</p>
  </article>

  <article class="abs card review-card" style="left:783px">
    <div class="stars"><svg width="94" height="18"><use href="#star"/><use href="#star" x="19"/><use href="#star" x="38"/><use href="#star" x="57"/><use href="#star" x="76"/></svg></div>
    <p class="review-text">Professional, knowledgeable, and dependable. We trust Kettlepoint with all our cooking equipment needs and know our kitchen is in good hands.</p>
    <div class="avatar" role="img" aria-label="Portrait photo of the reviewer"></div>
    <p class="reviewer">Helen T.,<br>General Manager</p>
  </article>

  <div class="abs arrow" style="left:39px;top:2379px;background:var(--brand)"><svg width="12" height="12" viewBox="0 0 12 12"><path d="M8 1L3 6l5 5" stroke="#fff" stroke-width="2.2" fill="none"/></svg></div>
  <div class="abs arrow" style="left:1129px;top:2379px;background:#5c9db1"><svg width="12" height="12" viewBox="0 0 12 12"><path d="M4 1l5 5-5 5" stroke="#fff" stroke-width="2.2" fill="none"/></svg></div>
</section>

<section>
  <h2 class="abs section-title" style="top:2696px">Request Service <b>or Get in Touch</b></h2>
  <div class="abs field" style="left:109px;top:2777px;width:466px">
    <svg width="16" height="16" viewBox="0 0 16 16"><circle cx="8" cy="4.5" r="3.5" fill="#777"/><path d="M1 16a7 6 0 0 1 14 0z" fill="#777"/></svg>Name</div>
  <div class="abs field" style="left:616px;top:2777px;width:473px">
    <svg width="22" height="20" viewBox="0 0 22 20"><rect x="4" y="1" width="12" height="11" fill="none" stroke="#777" stroke-width="1.6"/><path d="M7 5h6M7 8h4" stroke="#777" stroke-width="1.4"/><path d="M1 14l5-2 5 2h6l3 3-9 2-10-3z" fill="#777"/></svg>Service Request
    <svg style="position:absolute;right:34px" width="14" height="9" viewBox="0 0 14 9"><path d="M1 1l6 6 6-6" stroke="#333" stroke-width="1.6" fill="none"/></svg></div>
  <div class="abs field" style="left:109px;top:2848px;width:466px">
    <svg width="18" height="13" viewBox="0 0 18 13"><rect x="1" y="1" width="16" height="11" fill="none" stroke="#777" stroke-width="1.6"/><path d="M1 1l8 6 8-6" stroke="#777" stroke-width="1.6" fill="none"/></svg>Email</div>
  <div class="abs field" style="left:616px;top:2848px;width:473px;padding-left:30px">
    <svg width="17" height="17" viewBox="0 0 24 24"><path fill="#777" d="M6.6 10.8a15 15 0 0 0 6.6 6.6l2.2-2.2c.3-.3.7-.4 1-.2 1.1.4 2.3.6 3.6.6.6 0 1 .4 1 1V20c0 .6-.4 1-1 1A17 17 0 0 1 3 4c0-.6.4-1 1-1h3.5c.6 0 1 .4 1 1 0 1.3.2 2.5.6 3.6.1.3 0 .7-.2 1z"/></svg>Phone Number</div>
  <a class="abs btn" style="left:518px;top:2923px;width:164px;height:47px">Submit</a>
</section>

<footer class="abs site-footer"></footer>
<span class="abs foot-brand">Kettlepoint</span>
<span class="abs social" style="left:121px"></span>
<span class="abs social" style="left:157px"></span>
<span class="abs social" style="left:193px"></span>
<span class="abs social" style="left:229px"></span>

<h4 class="abs foot-head" style="left:410px">Quick Links</h4>
<ul class="abs foot-list" style="left:411px;top:3171px">
  <li class="sq">Home</li><li class="sq">About Us</li><li class="sq">Services</li><li class="sq">Testimonials</li><li class="sq">Contact</li>
</ul>
<h4 class="abs foot-head" style="left:619px">Help Links</h4>
<ul class="abs foot-list" style="left:620px;top:3171px">
  <li class="sq">Privacy Policy</li><li class="sq">Terms and Conditions</li><li class="sq">Cookies</li>
</ul>
<h4 class="abs foot-head" style="left:887px">Contact Us</h4>
<ul class="abs foot-list" style="left:887px;top:3171px">
  <li><svg width="22" height="22" viewBox="0 0 22 22"><circle cx="11" cy="11" r="11" fill="#fff"/><path fill="#0d6079" d="M8 9.5a9 9 0 0 0 4.5 4.5l1.4-1.4c.2-.2.5-.2.7-.1l1.9.4v2.6c0 .3-.2.5-.5.5A10 10 0 0 1 5.5 5.5c0-.3.2-.5.5-.5h2.6l.4 1.9c.1.2 0 .5-.1.7z"/></svg>+1 555 010 0199</li>
  <li style="margin-top:4px"><svg width="22" height="22" viewBox="0 0 22 22"><circle cx="11" cy="11" r="11" fill="#fff"/><rect x="5.5" y="7" width="11" height="8" fill="none" stroke="#0d6079" stroke-width="1.4"/><path d="M5.5 7l5.5 4 5.5-4" stroke="#0d6079" stroke-width="1.4" fill="none"/></svg>info@kettlepoint.example</li>
  <li style="margin-top:6px;align-items:flex-start;height:auto;line-height:26px"><svg style="margin-top:2px" width="22" height="22" viewBox="0 0 22 22"><circle cx="11" cy="11" r="11" fill="#fff"/><path fill="#0d6079" d="M11 4a5 5 0 0 0-5 5c0 4 5 9 5 9s5-5 5-9a5 5 0 0 0-5-5zm0 7a2 2 0 1 1 0-4 2 2 0 0 1 0 4z"/></svg><span>45 Harbor Lane, City,<br>State, ZIP</span></li>
</ul>
<div class="abs foot-rule"></div>
<p class="abs copyright">© 2025 Kettlepoint. All rights reserved.</p>

</body>
</html>
```